Simple
Garrick Holloway DDS, MS, PC
Orthodontics
Please Note I have four offices and need a business card for each. Below is the information for each office to be listed beside the logo on the business cards: Garrick Holloway DDS, MS Board Certified Orthodontist Salt Lake Office Cedar Hollow Professional Bldg 3815 South 700 East Suite F Pinecrest, Utah 84129 801 439 2106 ghbraces.example Garrick Holloway DDS, MS Board Certified Orthodontist Harvest Ridge Office 1847 West Juniper Bend Drive Suite 140 Brookvale, Utah 84051 801 592 3081 ghbraces.example Garrick Holloway DDS, MS Board Certified Orthodontist Kemmerer/ Diamondville Office 200 Mesa Lane Diamondville, Wyoming 83116 307 614 2839 ghbraces.example Garrick Holloway DDS, MS Board Certified Orthodontist Alder Creek Office 246 North 300 West Alder Creek, Utah 84093 801 683 1952 ghbraces.example
info@ghbraces.example
ghbraces.example
For the stationery I need the following: Letterhead: 2 Separate Letterheads with two office addresses per letterhead. Letterhead #1 to contain the following: Logo with these two addresses: Harvest Ridge Office 1847 West Juniper Bend Drive Suite 140 Brookvale, Utah 84051 801 592 3081 Alder Creek Office 246 North 300 West Alder Creek, Utah 84093 801 683 1952 Also on the Letterhead at the bottom of the page the following should be placed on one line: Garrick Holloway DDS, MS Board Certified Orthodontist Letterhead #2 to contain the following: Logo plus these two addresses: Salt Lake Office Cedar Hollow Professional Bldg 3815 South 700 East Suite F Pinecrest, Utah 84129 801 439 2106 Kemmerer/ Diamondville Office 200 Mesa Lane Diamondville, Wyoming 83116 307 614 2839 Also on the Letterhead at the bottom of the page should be placed the following on one line: Garrick Holloway DDS, MS Board Certified Orthodontist Envelopes: I need two letterhead envelopes: Letterhead Envelope #1 to contain Logo plus this return address: 1847 West Juniper Bend Drive Suite 140 Brookvale, Utah 84051 Letterhead Envelope #2 to contain Logo plus this return address: Cedar Hollow Professional Bldg 3815 South 700 East Suite F Pinecrest, Utah 84129 Other Envelopes: Billing Envelope is #10 Size with a window to contain Logo with this return address: 1847 West Juniper Bend Drive Suite 140 Brookvale, Utah 84051 Remittance Envelope: Size 6 3/4 (3 5/8 inch by 6 1/2 inch), to contain blank return address location and the following address in the addressee location front center of envelope: Garrick Holloway DDS, MS, PC Orthodontics 1847 West Juniper Bend Drive Suite 140 Brookvale, Utah 84051 The #10 billing Envelope and the # 6 3/4 Remittance envelopes are white. The Letterhead sheets and envelopes are Torvell papers, linen sheen, off white in color. Any questions pleas email. Thanks, GH

```html
<!DOCTYPE html>
<html lang="en">
<head>
<meta charset="utf-8">
<title>Garrick Holloway Orthodontics — Stationery</title>
<link rel="stylesheet" href="https://fonts.googleapis.com/css2?family=Cinzel:wght@500&family=Cormorant+Garamond:wght@500;600&display=swap">
<style>
  :root{
    --stage:#b3b3b3;
    --paper:#ffffff;
    --green:#8cc63f;
    --green-dark:#6fa82a;
    --ink:#4a4a4a;
    --window:#6d6d6d;
  }
  *{box-sizing:border-box;margin:0;padding:0}
  html,body{width:1200px;height:871px;overflow:hidden;background:var(--stage)}
  body{position:relative;font-family:"Cormorant Garamond",Georgia,serif;color:var(--ink)}
  .piece{position:absolute;background:var(--paper);overflow:hidden;box-shadow:0 2px 6px rgba(0,0,0,.25)}
  .piece svg.bands{position:absolute;inset:0;width:100%;height:100%}
  .brand{position:absolute;display:flex;align-items:center;gap:6px}
  .brand-square{width:9px;height:9px;background:var(--green)}
  .brand-name{font-family:"Cinzel",Georgia,serif;font-weight:500;color:var(--green-dark);letter-spacing:.5px;white-space:nowrap}
  .address{position:absolute;font-size:9px;line-height:1.3;font-weight:500;white-space:nowrap}
  .footer-line{position:absolute;left:0;right:0;text-align:center;color:#fff;font-family:"Cinzel",Georgia,serif;font-size:9px;letter-spacing:.8px;white-space:nowrap}

  /* letterhead */
  .letterhead{left:14px;top:12px;width:430px;height:556px}
  .letterhead .brand{left:28px;top:30px}
  .letterhead .brand-name{font-size:17px}
  .letterhead .address.office-a{left:38px;top:62px}
  .letterhead .address.office-b{right:30px;top:28px;text-align:left}
  .letterhead .footer-line{bottom:10px}

  /* billing window envelope */
  .billing-envelope{left:480px;top:56px;width:460px;height:212px}
  .billing-envelope .brand{left:34px;top:30px}
  .billing-envelope .brand-name{font-size:14px}
  .billing-envelope .address{left:44px;top:54px;font-size:8px}
  .address-window{position:absolute;left:190px;top:118px;width:180px;height:46px;border-radius:6px;background:var(--window)}

  /* letterhead envelope */
  .letter-envelope{left:620px;top:300px;width:470px;height:218px}
  .letter-envelope .brand{left:30px;top:34px}
  .letter-envelope .brand-name{font-size:14px}
  .letter-envelope .address{left:40px;top:58px;font-size:8px}

  /* business card */
  .business-card{left:760px;top:590px;width:252px;height:146px}
  .business-card .brand{left:18px;top:22px}
  .business-card .brand-name{font-size:11px}
  .business-card .address{left:22px;top:44px;font-size:7.5px}

  /* remittance envelope */
  .remittance-envelope{left:106px;top:632px;width:376px;height:206px}
  .remittance-envelope .brand{left:20px;top:20px}
  .remittance-envelope .brand-name{font-size:12px}
  .return-box{position:absolute;left:18px;top:118px;width:74px;height:48px;border:1px solid var(--ink);border-radius:4px;font-size:7px;padding:6px 8px}
  .remittance-envelope .address.addressee{left:160px;top:84px;font-size:8.5px}
</style>
</head>
<body>

<section class="piece letterhead" aria-label="Letterhead">
  <svg class="bands" viewBox="0 0 430 556" preserveAspectRatio="none" aria-hidden="true">
    <path d="M0 496 C120 470 300 470 430 420 L430 556 L0 556 Z" fill="var(--green)"/>
    <path d="M0 490 C120 462 300 462 430 412 L430 418 C300 468 120 468 0 494 Z" fill="var(--green)" opacity=".45"/>
  </svg>
  <div class="brand"><span class="brand-square"></span><span class="brand-name">Garrick Holloway</span></div>
  <p class="address office-a">Harvest Ridge Office<br>1847 West Juniper Bend Drive Suite 140<br>Brookvale, Utah 84051<br>801 592 3081</p>
  <p class="address office-b">Alder Creek Office<br>246 North 300 West<br>Alder Creek, Utah 84093<br>801 683 1952</p>
  <p class="footer-line">Garrick Holloway DDS, MS Board Certified Orthodontist</p>
</section>

<section class="piece billing-envelope" aria-label="Billing envelope">
  <svg class="bands" viewBox="0 0 460 212" preserveAspectRatio="none" aria-hidden="true">
    <path d="M0 0 L460 0 L460 10 C330 26 150 14 0 20 Z" fill="var(--green)"/>
    <path d="M0 196 C160 188 320 170 460 120 L460 212 L0 212 Z" fill="var(--green)"/>
  </svg>
  <div class="brand"><span class="brand-square"></span><span class="brand-name">Garrick Holloway</span></div>
  <p class="address">1847 West Juniper Bend Drive Suite 140<br>Brookvale, Utah 84051</p>
  <div class="address-window"></div>
</section>

<section class="piece letter-envelope" aria-label="Letterhead envelope">
  <svg class="bands" viewBox="0 0 470 218" preserveAspectRatio="none" aria-hidden="true">
    <path d="M0 0 L470 0 L470 12 C330 28 150 16 0 22 Z" fill="var(--green)"/>
    <path d="M0 204 C160 196 330 176 470 124 L470 218 L0 218 Z" fill="var(--green)"/>
  </svg>
  <div class="brand"><span class="brand-square"></span><span class="brand-name">Garrick Holloway</span></div>
  <p class="address">Cedar Hollow Professional Bldg<br>3815 South 700 East Suite F<br>Pinecrest, Utah 84129</p>
</section>

<section class="piece business-card" aria-label="Business card">
  <svg class="bands" viewBox="0 0 252 146" preserveAspectRatio="none" aria-hidden="true">
    <path d="M0 0 L252 0 L252 8 C170 20 80 10 0 14 Z" fill="var(--green)"/>
    <path d="M0 134 C90 128 180 116 252 88 L252 146 L0 146 Z" fill="var(--green)"/>
  </svg>
  <div class="brand"><span class="brand-square"></span><span class="brand-name">Garrick Holloway</span></div>
  <p class="address">Garrick Holloway DDS, MS<br>Board Certified Orthodontist<br>Harvest Ridge Office<br>1847 West Juniper Bend Drive Suite 140<br>Brookvale, Utah 84051 · 801 592 3081<br>ghbraces.example</p>
</section>

<section class="piece remittance-envelope" aria-label="Remittance envelope">
  <svg class="bands" viewBox="0 0 376 206" preserveAspectRatio="none" aria-hidden="true">
    <path d="M0 0 L376 0 L376 8 C260 20 120 10 0 16 Z" fill="var(--green)"/>
    <path d="M0 192 C130 186 270 172 376 140 L376 206 L0 206 Z" fill="var(--green)"/>
  </svg>
  <div class="brand"><span class="brand-square"></span><span class="brand-name">Garrick Holloway</span></div>
  <div class="return-box">Return Address</div>
  <p class="address addressee">Garrick Holloway DDS, MS, PC<br>Orthodontics<br>1847 West Juniper Bend Drive<br>Suite 140<br>Brookvale, Utah 84051</p>
</section>

</body>
</html>
```